2 graphics needed for brochure

I have 2 graphs needed for a brochure that our group is producing. They need to convey a high tech and innovation approach.

Industry/Entity Type

Graphic Design

```html
<!DOCTYPE html>
<html lang="en">
<head>
<meta charset="utf-8">
<title>Management/Resolution by Academic and Industry Collaborator</title>
<link rel="stylesheet" href="https://fonts.googleapis.com/css2?family=Pathway+Gothic+One&family=Oswald:wght@700&family=Lato:wght@400&display=swap">
<style>
  :root {
    --bg: #ffffff;
    --ink: #1a1a1a;
    --sky: #1cb0ea;
    --orange: #f7931e;
    --green: #7cc242;
    --violet: #c24ef0;
  }
  html, body {
    margin: 0;
    padding: 0;
    width: 1200px;
    height: 984px;
    overflow: hidden;
    background: var(--bg);
  }
  .canvas {
    position: relative;
    width: 1200px;
    height: 984px;
    background: var(--bg);
  }
  .title {
    position: absolute;
    top: 48px;
    left: 0;
    width: 1200px;
    margin: 0;
    text-align: center;
    font-family: "Pathway Gothic One", sans-serif;
    font-weight: 400;
    font-size: 54px;
    line-height: 72px;
    letter-spacing: 1.5px;
    color: var(--ink);
    text-transform: uppercase;
  }
  .frame {
    position: absolute;
    left: 0;
    top: 0;
  }
  .steps {
    list-style: none;
    margin: 0;
    padding: 0;
  }
  .step {
    position: absolute;
    left: 125px;
    width: 980px;
    display: flex;
    align-items: flex-start;
  }
  .step-number {
    flex: 0 0 53px;
    font-family: "Oswald", sans-serif;
    font-weight: 700;
    font-size: 33px;
    line-height: 36px;
    margin-top: -3px;
  }
  .step-text {
    font-family: "Lato", sans-serif;
    font-size: 22px;
    line-height: 30px;
    color: var(--ink);
  }
  .step-text .wrap { padding-left: 7px; }
  .sky { color: var(--sky); }
  .orange { color: var(--orange); }
  .green { color: var(--green); }
  .violet { color: var(--violet); }
</style>
</head>
<body>
<main class="canvas">
  <h1 class="title">Management/Resolution by Academic<br>and Industry Collaborator</h1>

  <svg class="frame" width="1200" height="984" viewBox="0 0 1200 984" aria-hidden="true">
    <rect x="52" y="224" width="1096" height="730" rx="8" fill="none"
          stroke="var(--sky)" stroke-width="4.5" stroke-linecap="round" stroke-dasharray="0 8"/>
    <rect x="62" y="239" width="1071" height="694" rx="14" fill="none"
          stroke="var(--orange)" stroke-width="5"/>
  </svg>

  <ol class="steps">
    <li class="step" style="top:284px">
      <span class="step-number sky">1.</span>
      <span class="step-text">Understanding what each party seeks and receives from any partnership.</span>
    </li>
    <li class="step" style="top:375px">
      <span class="step-number orange">2.</span>
      <span class="step-text">Formal disclosure of personal financial or other relationships for investigators and<br><span class="wrap">faculty researchers involved in project.</span></span>
    </li>
    <li class="step" style="top:498px">
      <span class="step-number green">3.</span>
      <span class="step-text">Review by organizational and other representatives as needed, to assess and<br><span class="wrap">provide recommendations for managing these relationships.</span></span>
    </li>
    <li class="step" style="top:617px">
      <span class="step-number violet">4.</span>
      <span class="step-text">Recommendation by independent officials on how to address any situation.</span>
    </li>
    <li class="step" style="top:708px">
      <span class="step-number sky">5.</span>
      <span class="step-text">Management/Resolution by academic parties in conjunction with their institutions,<br><span class="wrap">as well as management plans by industry.</span></span>
    </li>
    <li class="step" style="top:829px">
      <span class="step-number green">6.</span>
      <span class="step-text">Appropriate contract mechanisms that reflect proposed workplan and<br><span class="wrap">management plan.</span></span>
    </li>
  </ol>
</main>
</body>
</html>
```